Zia Bortolo's Cialdine

Looking for a packaging Label for Italian cookies. It has started with my great grandmothers Pizzelle recipe. Recipe has been in the family for over 100 years.
The packaging will be either clear plastic bags or Clear plastic hinged containers. Hoping for something elegant but traditional Italian. I have attached the company logo for color and idea possibilities
Would also like to give donation to helping animal foundations

Target Market(s)

Cookie lovers, coffee and tea drinkers, lighter alternative to heavy cookies

Requirements
Nice to have
• Family, Italian tradition

```html
<!DOCTYPE html>
<html lang="en">
<head>
<meta charset="utf-8">
<title>Zia Bortolo's Cialdine – Pizzelle Label</title>
<link href="https://fonts.googleapis.com/css2?family=Lato:wght@700&family=Oswald:wght@300;400&family=Alfa+Slab+One&family=Cinzel:wght@700&display=swap" rel="stylesheet">
<style>
  :root {
    --backdrop: #cbcbcb;
    --label-white: #ffffff;
    --ring-grey: #a9a9a9;
    --ornament-grey: #e6e6e6;
    --brand-orange: #e8560f;
    --ink: #1e1e1e;
  }
  html, body {
    margin: 0;
    padding: 0;
    width: 1200px;
    height: 827px;
    overflow: hidden;
    background: var(--backdrop);
  }
  .canvas {
    position: relative;
    width: 1200px;
    height: 827px;
  }
  .label {
    position: absolute;
    left: 205px;
    top: 18px;
    width: 790px;
    height: 790px;
    border-radius: 50%;
    background: var(--label-white);
  }
  .label-face {
    position: absolute;
    inset: 11px;
    border-radius: 50%;
    border: 5px solid var(--ring-grey);
    overflow: hidden;
    background: var(--label-white);
  }
  .brand {
    position: absolute;
    top: 180px;
    left: 0;
    right: 0;
    display: flex;
    justify-content: center;
    align-items: center;
    gap: 14px;
  }
  .brand-mark {
    width: 26px;
    height: 26px;
    border-radius: 50%;
    background: var(--brand-orange);
  }
  .brand-name {
    font-family: "Lato", sans-serif;
    font-weight: 700;
    font-size: 52px;
    color: var(--brand-orange);
    line-height: 1;
    margin: 0;
  }
  .pizzelle-ornament {
    position: absolute;
    left: 50%;
    top: 325px;
    width: 357px;
    height: 357px;
    margin-left: -178px;
    border-radius: 50%;
    background: radial-gradient(circle, #f7f7f7 0%, var(--ornament-grey) 70%, #f3f3f3 100%);
    opacity: 0.7;
  }
  .product-kicker {
    position: absolute;
    top: 420px;
    left: 0;
    right: 0;
    display: flex;
    justify-content: center;
    align-items: center;
    gap: 10px;
    font-family: "Oswald", sans-serif;
    font-weight: 400;
    font-size: 28px;
    line-height: 38px;
    letter-spacing: 1px;
    color: var(--ink);
  }
  .product-name {
    position: absolute;
    top: 458px;
    left: 0;
    right: 0;
    text-align: center;
    font-family: "Alfa Slab One", serif;
    font-weight: 400;
    font-size: 92px;
    letter-spacing: 3px;
    line-height: 110px;
    color: var(--brand-orange);
    margin: 0;
  }
  .heritage-band {
    position: absolute;
    top: 574px;
    left: 0;
    right: 0;
    height: 42px;
    background: var(--brand-orange);
    display: flex;
    align-items: center;
    justify-content: center;
    font-family: "Cinzel", serif;
    font-weight: 700;
    font-size: 22px;
    letter-spacing: 0.5px;
    color: var(--label-white);
  }
  .net-weight {
    position: absolute;
    top: 688px;
    left: 0;
    right: 0;
    text-align: center;
    font-family: "Oswald", sans-serif;
    font-weight: 300;
    font-size: 26px;
    line-height: 36px;
    color: var(--ink);
  }
</style>
</head>
<body>
<main class="canvas">
  <section class="label">
    <div class="label-face">
      <header class="brand">
        <span class="brand-mark"></span>
        <p class="brand-name">Zia Bortolo's</p>
      </header>

      <div class="pizzelle-ornament" role="img" aria-label="Faint grey pizzelle waffle pattern ornament behind the product name"></div>

      <div class="product-kicker">
        <svg width="56" height="12" viewBox="0 0 56 12"><path d="M2 8 Q15 2 28 6 T54 4" fill="none" stroke="var(--ink)" stroke-width="2"/></svg>
        <span>TRADITIONAL ITALIAN COOKIES</span>
        <svg width="56" height="12" viewBox="0 0 56 12"><path d="M2 4 Q15 10 28 6 T54 8" fill="none" stroke="var(--ink)" stroke-width="2"/></svg>
      </div>

      <h1 class="product-name">PIZZELLE</h1>

      <div class="heritage-band">100 YEARS OLD ORIGINAL RECIPE</div>

      <div class="net-weight">NET WT 10 oz (283 g)</div>
    </div>
  </section>
</main>
</body>
</html>
```